Falcon ridge RV Retreat business card

I need a design card for the logo I just had made on here. I will provide it and please make some cool designs, thank you.

I would like the card to have
- phone number (865-219-7652)
- email ( falconridgerv@examplemail.com)
- address to the park ( 5186 Copper Kettle Hollow rd, Maryville, TN) ZIP: 37946
on the back for double sided id like some lines for writing on. thanks

please follow the logo we provided in the files, I can provide the photoshop file if you need it.

please note this is in the Smokey mountains of Tennessee

Target Market(s)

cabin/rv rentals

Industry/Entity Type

rv/campground/cabin rentals

Contact Information for Business Card

address/email/phone number I added details in brief

Requirements
Must have
• on the back add a bear or something cool

```html
<!DOCTYPE html>
<html lang="en">
<head>
<meta charset="utf-8">
<title>Falcon Ridge RV Retreat – Business Card</title>
<link rel="stylesheet" href="https://fonts.googleapis.com/css2?family=Cinzel:wght@600&family=Roboto:wght@400;500&display=swap">
<style>
  :root {
    --bg: #1b1b1c;
    --sky-light: #7ea2c5;
    --sky-mid: #5583ab;
    --forest-dark: #141a17;
    --band-blue: #4f7fa8;
    --band-blue-light: #6f98c0;
    --ink: #1a1f24;
    --paper: #ffffff;
    --line: #c9d2da;
    --icon: #3f6f98;
  }
  * { box-sizing: border-box; margin: 0; padding: 0; }
  html, body { width: 1200px; height: 800px; overflow: hidden; }
  body { background: var(--bg); position: relative; }

  .card {
    position: absolute;
    top: 245px;
    width: 540px;
    height: 310px;
    border-radius: 16px;
    overflow: hidden;
  }
  .card--back { left: 40px; }
  .card--front { left: 620px; background: var(--paper); }
  .card__art { position: absolute; inset: 0; }

  /* back side */
  .scene {
    position: absolute; inset: 0;
    background: linear-gradient(180deg, var(--sky-light) 0%, var(--sky-mid) 32%, #2b3c40 50%, var(--forest-dark) 62%, var(--forest-dark) 100%);
  }
  .bear {
    position: absolute; left: 70px; top: 120px; width: 170px; height: 190px;
    border-radius: 60px 70px 0 0;
    background: linear-gradient(160deg, #e9ecee 0%, #b9c0c4 60%, #6f777b 100%);
  }
  .brand {
    position: absolute; display: flex; align-items: center; gap: 10px;
    font-family: "Cinzel", serif; font-weight: 600; letter-spacing: 0.04em;
    white-space: nowrap;
  }
  .brand__dot { width: 22px; height: 22px; border-radius: 50%; flex: none; }
  .brand--back { left: 210px; top: 70px; font-size: 15px; color: var(--paper); }
  .brand--back .brand__dot { width: 26px; height: 26px; background: #f0b04a; }
  .write-lines { position: absolute; left: 290px; top: 135px; width: 225px; }
  .write-lines span { display: block; height: 1px; background: var(--line); margin-bottom: 44px; }

  /* front side */
  .holder {
    position: absolute; right: 36px; top: 40px; text-align: right; color: var(--ink);
  }
  .holder__name { font-family: "Cinzel", serif; font-weight: 600; font-size: 20px; letter-spacing: 0.06em; }
  .holder__title { font-family: "Roboto", sans-serif; font-weight: 500; font-size: 12px; }
  .brand--front { left: 58px; top: 222px; font-size: 14px; color: var(--ink); }
  .brand--front .brand__dot { background: var(--band-blue); }
  .contact {
    position: absolute; left: 58px; top: 252px; list-style: none;
    font-family: "Roboto", sans-serif; font-size: 12px; color: var(--ink); line-height: 18px;
  }
  .contact li { display: flex; align-items: center; gap: 8px; }
  .contact svg { width: 11px; height: 11px; fill: var(--icon); flex: none; }
  .address {
    position: absolute; right: 36px; top: 190px; text-align: right; font-style: normal;
    font-family: "Roboto", sans-serif; font-size: 12px; color: var(--ink); line-height: 17px;
  }
</style>
</head>
<body>

<section class="card card--back">
  <div class="scene" role="img" aria-label="Smoky Mountain landscape with blue ridges and dark pine forest"></div>
  <div class="bear" role="img" aria-label="Sketched illustration of a standing bear"></div>
  <div class="brand brand--back"><span class="brand__dot"></span>Falcon Ridge RV Retreat</div>
  <div class="write-lines"><span></span><span></span><span></span></div>
</section>

<section class="card card--front">
  <svg class="card__art" viewBox="0 0 540 310" aria-hidden="true">
    <defs>
      <linearGradient id="bandGrad" x1="0" y1="0" x2="1" y2="0">
        <stop offset="0" stop-color="var(--band-blue)"/>
        <stop offset="0.6" stop-color="var(--band-blue-light)"/>
        <stop offset="1" stop-color="var(--band-blue)"/>
      </linearGradient>
    </defs>
    <path d="M0 0 H540 V85 C470 135 370 150 270 152 C150 154 60 170 0 235 Z" fill="url(#bandGrad)"/>
    <path d="M0 235 C60 170 150 154 270 152 C370 150 470 135 540 85 V97 C470 150 370 162 270 163 C160 166 70 190 0 252 Z" fill="var(--ink)"/>
    <path d="M330 140 C420 138 500 108 540 58 V70 C500 122 420 146 330 140 Z" fill="var(--paper)"/>
  </svg>

  <div class="holder">
    <p class="holder__name">Daniel Harper</p>
    <p class="holder__title">President</p>
  </div>

  <div class="brand brand--front"><span class="brand__dot"></span>Falcon Ridge RV Retreat</div>

  <ul class="contact">
    <li><svg viewBox="0 0 24 24"><path d="M6.6 10.8a15 15 0 0 0 6.6 6.6l2.2-2.2a1 1 0 0 1 1-.25 11.4 11.4 0 0 0 3.6.57 1 1 0 0 1 1 1V20a1 1 0 0 1-1 1A17 17 0 0 1 3 4a1 1 0 0 1 1-1h3.5a1 1 0 0 1 1 1c0 1.25.2 2.45.57 3.57a1 1 0 0 1-.25 1z"/></svg>(865-219-7652)</li>
    <li><svg viewBox="0 0 24 24"><path d="M2 5h20v14H2z M2 5l10 8 10-8" /></svg>falconridgerv@examplemail.com</li>
    <li><svg viewBox="0 0 24 24"><circle cx="12" cy="12" r="10"/></svg>falconridgerv.example</li>
  </ul>

  <address class="address">5186 Copper Kettle<br>Hollow rd<br>Maryville, TN: 37946</address>
</section>

</body>
</html>
```